Events Online Video Streaming Company

A website needs to be designed to replace the current website of a company that specialises in providing an online portal for streaming events to users. the current portal exists at: http://www.tazorin.com <- designers can get a "feel" for what they do and the content they require from this existing website.
the current tazorin logo and green color are to be maintined. i will upload an EPS of the logo soon.
The new design needs to highlight the main aspects of what they do: live streaming of events, multiple cameras, online chat, user activity data (like brindle metrics), customised front-ends.
we want the design to be in-between a corporate feel and modern, contemporary. ie. we dont want it to be too corporate (like the current website).
the design must also incorporate the word: fernoskaps as part of their slogan or sub-title.
hi everyone,

```html
<!DOCTYPE html>
<html lang="en">
<head>
<meta charset="utf-8">
<title>tazorin — online event streaming</title>
<link href="https://fonts.googleapis.com/css2?family=Ubuntu:ital,wght@0,400;0,500;0,700;1,400&display=swap" rel="stylesheet">
<style>
:root{
  --green:#8dc63f;
  --green-dark:#3f6d17;
  --header-top:#4d7e1c;
  --header-mid:#5e9626;
  --frame:#6fa637;
  --ink:#2b2b2b;
  --dark:#2a2927;
  --text-light:#e8e8e8;
  --card-gray:#3d3d3d;
  --card-teal:#1f6660;
  --card-green:#3f6d17;
  --card-orange:#c4471a;
  --card-silver:#8e8e8e;
}
*{margin:0;padding:0;box-sizing:border-box}
html,body{width:1089px;height:1200px;overflow:hidden}
body{position:relative;font-family:"Ubuntu",sans-serif;color:var(--text-light);
  background:radial-gradient(ellipse at 50% 62%,#4a4744 0%,var(--dark) 55%,#1f1e1d 100%)}
h2,h3,h4{font-weight:400}
.abs{position:absolute}
.header{left:0;top:0;width:1089px;height:493px;
  background:radial-gradient(ellipse at 50% 45%,#7ab33a 0%,var(--header-mid) 45%,var(--header-top) 100%)}
.logo{left:144px;top:22px;width:184px;height:72px;background:linear-gradient(#fff,#e4e4e4);
  display:flex;align-items:center;justify-content:center;gap:8px;box-shadow:0 3px 6px rgba(0,0,0,.35)}
.logo-name{font-size:38px;font-weight:400;color:var(--green-dark);letter-spacing:-1px}
.logo-dot{width:10px;height:10px;border-radius:50%;background:var(--green)}
.top-phone{left:836px;top:16px;font-size:14px;font-weight:700;color:#fff;display:flex;align-items:center;gap:5px}
.nav{left:415px;top:47px;width:530px;height:48px;background:#2f3f1c;display:flex;
  box-shadow:0 10px 12px -6px rgba(0,0,0,.45)}
.nav a{color:#fff;text-decoration:none;font-size:15.5px;display:flex;align-items:center;justify-content:center;
  border-right:1px solid #44552f}
.nav a.active{background:var(--green);color:var(--ink)}
.hero{left:144px;top:120px;width:800px;height:373px;background:var(--frame)}
.hero-photo{left:8px;top:8px;width:784px;height:326px;
  background:radial-gradient(ellipse at 75% 40%,#c7b8a8 0%,#a79a8c 30%,transparent 60%),
  linear-gradient(100deg,#e9e6e1 0%,#d8a878 35%,#b8c6c8 60%,#9ea7ad 100%)}
.hero-caption{left:8px;top:334px;width:784px;height:31px;background:rgba(20,20,20,.88);
  font-size:18px;font-style:italic;color:#fff;padding:4px 12px}
.dots{right:22px;top:10px;display:flex;gap:10px}
.dots span{width:14px;height:14px;border-radius:50%;background:#fff}
.dots span.on{background:var(--green)}
.card{top:498px;width:154px;height:195px;padding:20px 15px 0}
.card h3{font-size:17px;font-weight:400;line-height:18px;color:#fff}
.card h3 b{font-weight:700}
.card .rule{width:90px;height:1px;background:rgba(255,255,255,.35);margin-top:8px}
.card svg.icon{position:absolute;left:46px;top:78px}
.card .more{position:absolute;left:0;width:100%;top:167px;text-align:center;font-size:11.5px;color:var(--green)}
.card .fold{position:absolute;right:0;bottom:0}
.c1{left:144px;background:var(--card-gray);border-top:3px solid #5a5a5a}
.c2{left:305px;background:var(--card-teal);border-top:3px solid #34b3a8}
.c3{left:466px;background:var(--card-green);border-top:3px solid #6aaa2a}
.c4{left:627px;background:var(--card-orange);border-top:3px solid #e86a36}
.c5{left:789px;background:var(--card-silver);border-top:3px solid #c4c4c4}
.rule-wide{left:144px;width:800px;height:1px;background:linear-gradient(90deg,transparent,#5a5754,transparent)}
.welcome{left:0;width:1089px;top:718px;text-align:center;font-size:17px;color:#fff;font-weight:400}
.welcome b{font-size:28px;font-weight:400;margin-left:4px}
.intro{left:274px;top:769px;width:540px;text-align:center;font-size:10.5px;line-height:15.3px;color:#f2f2f2}
.features-title{left:0;width:1089px;top:880px;text-align:center;font-size:16px}
.feat{font-size:10.5px;text-transform:uppercase;list-style:none}
.feat li{height:33px}
.feat li::before{content:"•";color:var(--green);margin-right:7px}
.enquire{left:376px;top:996px;font-size:17px;color:var(--green)}
.call-btn{left:560px;top:991px;width:152px;height:32px;border-radius:3px;
  background:linear-gradient(#b5e06a,var(--green));color:#111;font-size:18px;font-weight:700;
  display:flex;align-items:center;justify-content:center}
.foot-h{top:1052px;font-size:11px;color:#fff}
.foot-list{list-style:none;font-size:10.5px;line-height:15.8px}
.foot-list li::before{content:"•";color:var(--green);margin-right:7px}
.contact-row{left:598px;font-size:10.5px;line-height:16px;display:flex;gap:10px}
.contact-row svg{flex:none;margin-top:2px}
.foot-logo{left:788px;top:1090px;font-size:34px;color:#bdbdbd;display:flex;align-items:center;gap:6px}
.foot-logo i{width:8px;height:8px;border-radius:50%;background:#bdbdbd;display:block}
.social{top:1147px;width:19px;height:19px;border-radius:3px;background:#bdbdbd}
.bottom{left:0;top:1176px;width:1089px;height:24px;background:#111;text-align:center;
  font-size:10px;line-height:24px;color:#9a9a9a}
</style>
</head>
<body>
<header class="abs header">
  <div class="abs logo"><span class="logo-name">tazorin</span><span class="logo-dot"></span></div>
  <div class="abs top-phone">
    <svg width="18" height="18" viewBox="0 0 18 18"><circle cx="9" cy="9" r="8" fill="none" stroke="#fff" stroke-width="1.3"/><path d="M6 5c-1 1 0 4 2 6s4 3 5 2l-1.5-1.5-1.3.8c-1-.5-2.3-1.8-2.8-2.8l.8-1.3z" fill="#fff"/></svg>
    1300 555 019
  </div>
  <nav class="abs nav">
    <a class="active" href="#" style="width:73px">home</a>
    <a href="#" style="width:81px">features</a>
    <a href="#" style="width:112px">applications</a>
    <a href="#" style="width:88px">the team</a>
    <a href="#" style="width:80px">support</a>
    <a href="#" style="width:96px;border-right:0">contact us</a>
  </nav>
  <section class="abs hero">
    <div class="abs hero-photo" role="img" aria-label="Photo of a smiling support agent wearing a headset, with a laptop showing a video call in the background"></div>
    <div class="abs hero-caption">specialize in providing an online portal for streaming events to users
      <div class="abs dots"><span class="on"></span><span></span><span></span><span></span></div>
    </div>
  </section>
</header>

<article class="abs card c1">
  <h3>live<br><b>streaming</b></h3><div class="rule"></div>
  <svg class="icon" width="62" height="62" viewBox="0 0 62 62"><circle cx="31" cy="31" r="28" fill="none" stroke="#7ab33a" stroke-width="3"/><circle cx="31" cy="27" r="14" fill="none" stroke="#7ab33a" stroke-width="2"/><circle cx="31" cy="27" r="8" fill="none" stroke="#7ab33a" stroke-width="2"/><path d="M31 25l-8 19h16z" fill="#7ab33a"/></svg>
  <div class="more">more+</div>
  <svg class="fold" width="28" height="28"><path d="M0 28L28 0v28z" fill="#2a2927"/><path d="M0 28L28 0H6z" fill="#777"/></svg>
</article>
<article class="abs card c2">
  <h3>multiple<br><b>cameras</b></h3><div class="rule"></div>
  <svg class="icon" width="62" height="62" viewBox="0 0 62 62"><circle cx="31" cy="31" r="28" fill="none" stroke="#7ab33a" stroke-width="3"/><rect x="15" y="22" width="32" height="20" rx="3" fill="none" stroke="#7ab33a" stroke-width="3"/><circle cx="33" cy="32" r="6" fill="none" stroke="#7ab33a" stroke-width="3"/></svg>
  <div class="more">more+</div>
  <svg class="fold" width="28" height="28"><path d="M0 28L28 0v28z" fill="#2a2927"/><path d="M0 28L28 0H6z" fill="#34b3a8"/></svg>
</article>
<article class="abs card c3">
  <h3>online<br><b>chat</b></h3><div class="rule"></div>
  <svg class="icon" width="62" height="62" viewBox="0 0 62 62"><circle cx="31" cy="31" r="28" fill="none" stroke="#7ab33a" stroke-width="3"/><ellipse cx="26" cy="28" rx="11" ry="8" fill="#7ab33a"/><ellipse cx="37" cy="34" rx="10" ry="7" fill="#a5d165"/></svg>
  <div class="more">more+</div>
  <svg class="fold" width="28" height="28"><path d="M0 28L28 0v28z" fill="#2a2927"/><path d="M0 28L28 0H6z" fill="#6aaa2a"/></svg>
</article>
<article class="abs card c4">
  <h3>user<br><b>activity data</b></h3><div class="rule"></div>
  <svg class="icon" width="62" height="62" viewBox="0 0 62 62"><circle cx="31" cy="31" r="28" fill="none" stroke="#7ab33a" stroke-width="3"/><rect x="19" y="20" width="24" height="22" rx="2" fill="none" stroke="#7ab33a" stroke-width="2.5"/><path d="M24 31l5 5 9-9" fill="none" stroke="#7ab33a" stroke-width="3"/></svg>
  <div class="more">more+</div>
  <svg class="fold" width="28" height="28"><path d="M0 28L28 0v28z" fill="#2a2927"/><path d="M0 28L28 0H6z" fill="#e86a36"/></svg>
</article>
<article class="abs card c5">
  <h3>customized<br><b>front-ends</b></h3><div class="rule"></div>
  <svg class="icon" width="62" height="62" viewBox="0 0 62 62"><circle cx="31" cy="31" r="28" fill="none" stroke="#4f8a1f" stroke-width="3"/><circle cx="31" cy="31" r="13" fill="none" stroke="#4f8a1f" stroke-width="6" stroke-dasharray="5 3.2"/><circle cx="31" cy="31" r="7" fill="none" stroke="#4f8a1f" stroke-width="4"/></svg>
  <div class="more">more+</div>
  <svg class="fold" width="28" height="28"><path d="M0 28L28 0v28z" fill="#2a2927"/><path d="M0 28L28 0H6z" fill="#ddd"/></svg>
</article>

<div class="abs rule-wide" style="top:709px"></div>
<h2 class="abs welcome">Welcome to <b>tazorin</b></h2>
<p class="abs intro">Lorem ipsum dolor sit amet, consectetuer adipiscing elit, sed diam nonummy nibh euismod tincidunt ut laoreet dolore magna aliquam erat volutpat. Ut wisi enim ad minim veniam, quis nostrud exerci tation ullamcorper suscipit lobortis nisl ut aliquip ex ea commodo consequat. Duis autem vel eum iriure dolor in hendrerit in vulputate velit esse molestie consequat, vel illum dolore eu feugiat nulla facilisis at vero eros et accumsan et iusto odio dignissim qui blandit praesent luptatum zzril delenit augue duis dolore te feugait nulla facilisi.</p>

<div class="abs rule-wide" style="top:872px"></div>
<h2 class="abs features-title">Our Features</h2>
<ul class="abs feat" style="left:151px;top:916px"><li>Secure event content</li><li>Latest technology</li></ul>
<ul class="abs feat" style="left:328px;top:916px"><li>Too busy to attend?</li><li>Global audience</li></ul>
<ul class="abs feat" style="left:489px;top:916px"><li>Mobile &nbsp;and tablet friendly</li><li>Chirply, Frendly, Worknet, chat</li></ul>
<ul class="abs feat" style="left:726px;top:916px"><li>Online event portal</li><li>Attend from anywhere in the world</li></ul>

<div class="abs enquire">For enquiries call us on</div>
<div class="abs call-btn">1300 555 019</div>
<div class="abs rule-wide" style="top:1035px"></div>

<footer>
  <h4 class="abs foot-h" style="left:166px">Quick Links</h4>
  <ul class="abs foot-list" style="left:172px;top:1073px"><li>home</li><li>features</li><li>applications</li><li>the team</li><li>support</li><li>contact us</li></ul>
  <h4 class="abs foot-h" style="left:290px">Services</h4>
  <ul class="abs foot-list" style="left:296px;top:1073px"><li>innovation / technology</li><li>social media, networking</li><li>live video streaming</li><li>video on demand</li><li>analytical reporting</li><li>sponsor/advertising</li></ul>
  <ul class="abs foot-list" style="left:454px;top:1073px"><li>any device, no install</li><li>easy to use</li></ul>
  <h4 class="abs foot-h" style="left:598px">Contact Us</h4>
  <div class="abs contact-row" style="top:1075px"><svg width="12" height="14" viewBox="0 0 12 14"><path d="M6 0a5 5 0 0 0-5 5c0 4 5 9 5 9s5-5 5-9a5 5 0 0 0-5-5z" fill="#8dc63f"/><circle cx="6" cy="5" r="2" fill="#2a2927"/></svg><span>012 Ut wisi enim ad minim<br>tation ullamcorper</span></div>
  <div class="abs contact-row" style="top:1112px"><svg width="12" height="13" viewBox="0 0 12 13"><path d="M2 1c-2 2 0 6 2 8s6 4 8 2l-2-2-2 1c-1-.5-3-2.5-3.5-3.5l1-2z" fill="#8dc63f"/></svg><span>1300 555 019</span></div>
  <div class="abs contact-row" style="top:1134px"><svg width="12" height="12" viewBox="0 0 12 12"><rect x="3" y="0" width="6" height="4" fill="#8dc63f"/><rect x="0" y="5" width="12" height="6" fill="#8dc63f"/></svg><span>1300 555 019</span></div>
  <div class="abs contact-row" style="top:1153px"><svg width="12" height="10" viewBox="0 0 12 10"><rect x="0" y="1" width="12" height="8" fill="#8dc63f"/><path d="M0 1l6 4 6-4" fill="none" stroke="#2a2927" stroke-width="1"/></svg><span>info@example.com</span></div>
  <div class="abs foot-logo"><span>tazorin</span><i></i></div>
  <a class="abs social" style="left:815px" aria-label="social link"></a>
  <a class="abs social" style="left:848px" aria-label="social link"></a>
  <a class="abs social" style="left:881px" aria-label="social link"></a>
  <div class="abs bottom">Copyright © 2103 tazorin &nbsp;| &nbsp;All Rights Reserved</div>
</footer>
</body>
</html>
```